Corkly Soy Candles - New WP TEMPLATE

We make handemade soy candles in large volume and our company is now seeing huge growth, we are about to break into the retail market by providing our candles wholesale to retail outlets and gift stores.

Our candles are set apart by the fact they are very earth friendly in the sense of utilising old wine bottles that are cut in half and filling them with highly scented all natural pure soy and sealing the candle with a cork.

The website will need to be a complete Wordpress template. PLEASE ensure it is responsive and mobile friendly.

The look and feel of the website will need to be very original and rustic in feel.

Some examples of the "feel" of the site cand be found at the following links:

http://www.example-plankstudio.test/blog/2011/07/new-website-launches-for-july/

http://www.example-fernhutcabin.test/

http://www.example-glowvatlights.test/

http://www.example-sage417.test/wedding-logo/rustic-ombre-summer-wedding-website/

http://example-plumthemes.test/grunge-website-design/screen-shot-2012-02-04-at-6-22-21-pm/

Our lettering logo is simply the word "Corkly" in the font "Sweetly Broken". I have included our WORD logo and our SYMBOL logo. You will see our product in the images attached.

The site should include:

A slider
All images to be in circle cut outs (not square)

-A homepage with slider
-A section for "The Story" (This will be the largest page with a circle for each of the 6 scents and then a staggered story line of how we make the candles, alternating pictures from left to right).
-A section for "Retailers"
-A section for "Wholesale"
-A contact section

Please place some sort of placeholder images in all of the areas that will have images - were having the images done professionally and I have some design experience so I can finalise this aspect.

If you can make this a "One page template" that would be okay, but we are also open to multipage designs as long as its user friendly.

See images for the process and feel of product.

IF you think the prize needs to be increased and you have a good design that we like, we are happy to negotiate with you!

```html
<!DOCTYPE html>
<html lang="en">
<head>
<meta charset="utf-8">
<title>Corkly Soy Candles</title>
<link rel="stylesheet" href="https://fonts.googleapis.com/css2?family=Overlock+SC&family=Raleway:wght@400&family=Sue+Ellen+Francisco&display=swap">
<style>
  :root {
    --paper: #dcd2cb;
    --paper-light: #e2d9d3;
    --slide-bg: #f8f8f8;
    --ink: #5b3b33;
    --ink-soft: #5f4e49;
    --rule: #a8978f;
    --button-line: #a99a93;
    --dot: #a59893;
    --dot-active: #5b3b33;
    --glass-light: #d8cf4a;
    --glass-mid: #8c8a2e;
    --glass-dark: #3f4020;
  }
  * { margin: 0; padding: 0; box-sizing: border-box; }
  html, body {
    width: 1200px;
    height: 953px;
    overflow: hidden;
  }
  body {
    position: relative;
    background: radial-gradient(ellipse at 40% 30%, var(--paper-light), var(--paper) 70%);
    color: var(--ink);
    font-family: "Overlock SC", Georgia, serif;
  }

  /* Header */
  .site-header { position: absolute; left: 0; top: 0; width: 1200px; height: 152px; }
  .brand {
    position: absolute; left: 69px; top: 38px;
    font-size: 64px; line-height: 1; color: var(--ink);
    letter-spacing: 1px;
  }
  .main-nav {
    position: absolute; right: 68px; top: 55px;
    height: 34px;
    border-top: 1px solid var(--rule);
    border-bottom: 1px solid var(--rule);
    display: flex; align-items: center; gap: 22px;
    padding-left: 3px;
  }
  .main-nav a {
    color: var(--ink); text-decoration: none;
    font-size: 20px; line-height: 1;
  }

  /* Slider */
  .slider {
    position: absolute; left: 0; top: 152px;
    width: 1200px; height: 420px;
    background: var(--slide-bg);
  }
  .slide-photo {
    position: absolute; left: 69px; top: 27px;
    width: 366px; height: 366px; border-radius: 50%;
    background:
      radial-gradient(circle at 55% 70%, var(--glass-light) 0%, rgba(216,207,74,0) 45%),
      radial-gradient(circle at 30% 40%, var(--glass-mid) 0%, var(--glass-dark) 85%);
  }
  .slide-title {
    position: absolute; left: 440px; top: 30px;
    font-family: "Sue Ellen Francisco", cursive;
    font-weight: 400; font-size: 76px; line-height: 1;
    color: var(--ink);
  }
  .slide-text {
    position: absolute; left: 467px; top: 143px; width: 630px;
    font-size: 19px; line-height: 25.5px; color: var(--ink);
  }
  .slide-text p + p { margin-top: 12px; }
  .btn {
    display: inline-flex; align-items: center; justify-content: center;
    border: 1px solid var(--button-line);
    color: var(--ink); text-decoration: none;
    font-family: "Overlock SC", Georgia, serif;
  }
  .slide-button {
    position: absolute; left: 467px; top: 313px;
    width: 168px; height: 52px; font-size: 20px;
  }
  .slider-dots {
    position: absolute; left: 560px; top: 595px;
    display: flex; gap: 15px;
  }
  .slider-dots span {
    width: 6px; height: 6px; border-radius: 50%; background: var(--dot);
  }
  .slider-dots span.is-active { background: var(--dot-active); }

  /* Feature columns */
  .feature {
    position: absolute; top: 630px; width: 334px;
  }
  .feature h2 {
    font-weight: 400; font-size: 27px; line-height: 1;
    color: var(--ink);
    padding: 4px 0 8px;
    border-bottom: 1px solid var(--rule);
  }
  .feature p {
    margin-top: 20px;
    font-family: "Raleway", Arial, sans-serif;
    font-size: 15.5px; line-height: 19px; color: var(--ink-soft);
  }
  .feature .btn {
    position: absolute; top: 176px; left: -2px;
    width: 136px; height: 42px; font-size: 17px;
  }
  .feature--retailers { left: 70px; }
  .feature--wholesalers { left: 435px; }
  .feature--story { left: 802px; }

  /* Footer */
  .site-footer {
    position: absolute; left: 70px; top: 900px; width: 1062px;
    border-top: 1px solid var(--rule);
    padding-top: 9px;
    font-family: "Raleway", Arial, sans-serif;
    font-size: 16px; color: #7a6b66;
  }
</style>
</head>
<body>
  <header class="site-header">
    <div class="brand">Corkly</div>
    <nav class="main-nav">
      <a href="#">Home</a>
      <a href="#">Our Story</a>
      <a href="#">Retailers</a>
      <a href="#">Wholesalers</a>
      <a href="#">Contact Us</a>
    </nav>
  </header>

  <section class="slider">
    <div class="slide-photo" role="img" aria-label="Circular photo of cut wine bottle halves standing together, olive green glass"></div>
    <h1 class="slide-title">Lorem Ipsum Dolor Sit</h1>
    <div class="slide-text">
      <p>Lorem ipsum dolor sit amet, consectetur adipiscing elit. Nunc pellentesque a leo non fringilla. Nulla semper porta odio at faucibus. Curabitur massa odio, iaculis vel felis eu, placerat vehicula metus. Mauris maximus tellus pretium metus iaculis euismod.</p>
      <p>Phasellus pharetra metus vitae odio placerat, quis accumsan ipsum tincidunt.</p>
    </div>
    <a class="btn slide-button" href="#">Read More</a>
  </section>

  <div class="slider-dots">
    <span class="is-active"></span><span></span><span></span><span></span><span></span>
  </div>

  <section class="feature feature--retailers">
    <h2>Retailers</h2>
    <p>Vivamus quis placerat nisi, vel tincidunt massa. Phasellus ut risus imperdiet, posuere velit quis, rhoncus neque. Nam sed lacinia massa. Quisque euismod porttitor odio nec luctus.</p>
    <a class="btn" href="#">Read More</a>
  </section>
  <section class="feature feature--wholesalers">
    <h2>Wholesalers</h2>
    <p>Vivamus quis placerat nisi, vel tincidunt massa. Phasellus ut risus imperdiet, posuere velit quis, rhoncus neque. Nam sed lacinia massa. Quisque euismod porttitor odio nec luctus.</p>
    <a class="btn" href="#">Read More</a>
  </section>
  <section class="feature feature--story">
    <h2>Our Story</h2>
    <p>Vivamus quis placerat nisi, vel tincidunt massa. Phasellus ut risus imperdiet, posuere velit quis, rhoncus neque. Nam sed lacinia massa. Quisque euismod porttitor odio nec luctus.</p>
    <a class="btn" href="#">Read More</a>
  </section>

  <footer class="site-footer">Copyright © Corkly Soy Candles, 2014 | Website by Lantern Row Studio</footer>
</body>
</html>
```